Young Adult Retreat Needs Event Promo Graphics

I need graphics designed for our summer young adult (18 years old - 30 years old) camp-style retreat. This event will take place at a campground in the black hills of South Dakota. Primary graphic design is for a 11x17 poster but will also need the images resized for:

-social media: square; can include only main titles or main titles and speaker
-16x9 title slide that includes: titles, full background images, organization logo, and website. No camp speaker or dates, no additional info.
- a postcard size (4.25in x 6in) with all content on it

All graphics need to be print quality (300 dpi or higher)

11x17 main poster design should include the following:
-Main Title: PR Brightway (or logo) presents . . . South Dakota Young Adult Retreat
-Dates: June 3-5th, 2022
-Register at PRBrightway.com
-Cedar Ridge Lodge Center, Deadwood, SD
-Speaker: Marla Pettigrew (photo attached)
-Include PR Brightway logo
-Event Graphic should be attractive to 18-30 year olds but SHOULD NOT include references to alcohol, sexuality, drugs, or profanity.

My graphic design experience is limited. I will need help receiving the files I need in the various sizes. Thank you.

```html
<!DOCTYPE html>
<html lang="en">
<head>
<meta charset="utf-8">
<title>South Dakota Young Adult Retreat — Poster</title>
<link href="https://fonts.googleapis.com/css2?family=Alfa+Slab+One&family=Roboto+Slab:wght@400;700;900&family=Montserrat:ital,wght@1,500&display=swap" rel="stylesheet">
<style>
  :root {
    --ink: #0d0d10;
    --night: #16171c;
    --royal: #2e3794;
    --sky: #2aa9e2;
    --snow: #f1f1ef;
    --paper: #d9d9d7;
    --text-dark: #2a2a2e;
    --dusk-blue: #3d5bbd;
    --dusk-violet: #8a7ab8;
    --dusk-pink: #d59bb5;
  }
  * { margin: 0; padding: 0; box-sizing: border-box; }
  html, body { width: 800px; height: 1200px; overflow: hidden; background: var(--ink); }
  .poster { position: relative; width: 800px; height: 1200px; overflow: hidden; background: var(--night); font-family: "Roboto Slab", serif; }

  .sky { position: absolute; inset: 0 0 auto 0; height: 520px;
    background: linear-gradient(170deg, var(--dusk-blue) 0%, #5c76d0 25%, var(--dusk-violet) 50%, var(--dusk-pink) 75%, #b38aa8 100%); }
  .moon { position: absolute; left: 150px; top: 12px; width: 500px; height: 500px; border-radius: 50%; background: var(--snow); }
  .mountain-forest { position: absolute; left: 0; top: 215px; width: 800px; height: 360px;
    background: linear-gradient(180deg, rgba(155,90,69,0) 0%, rgba(155,90,69,0.95) 12%, #7a4a44 35%, #2b2626 65%, var(--night) 100%); }
  .crowd-photo { position: absolute; left: 0; top: 810px; width: 500px; height: 200px;
    background: radial-gradient(ellipse at 55% 50%, rgba(120,120,120,0.35), rgba(22,23,28,0) 70%); }

  .brand { position: absolute; top: 68px; width: 100%; text-align: center; font-weight: 900; font-size: 46px; line-height: 1.1; color: var(--sky); }
  .presents { position: absolute; top: 196px; width: 100%; text-align: center; font-family: "Montserrat", sans-serif; font-style: italic; font-weight: 500; font-size: 17px; letter-spacing: 6px; color: var(--text-dark); }

  .title-band { position: absolute; left: 60px; top: 522px; width: 730px; height: 275px; }
  .title { position: absolute; top: 534px; width: 100%; text-align: center; line-height: 1; }
  .title-region { display: block; font-weight: 700; font-size: 52px; color: var(--snow); letter-spacing: 1px; }
  .title-group { display: block; font-weight: 700; font-size: 66px; color: var(--snow); margin-top: 4px; }
  .title-main { display: block; font-weight: 900; font-size: 112px; color: var(--sky); margin-top: 0; letter-spacing: 2px; }

  .dates { position: absolute; left: 98px; top: 822px; display: flex; align-items: center; gap: 12px; }
  .dates-text { font-family: "Alfa Slab One", serif; line-height: 1; white-space: nowrap; }
  .dates-days { font-size: 60px; color: var(--sky); }
  .dates-days sup { font-size: 26px; vertical-align: 28px; }
  .dates-month { font-size: 58px; color: var(--snow); margin-top: 6px; }
  .dates-year { flex: none; width: 40px; height: 118px; background: var(--royal);
    display: flex; align-items: center; justify-content: center; }
  .dates-year span { display: block; transform: rotate(90deg); font-family: "Alfa Slab One", serif; font-size: 26px; line-height: 1; color: var(--sky); white-space: nowrap; }

  .speaker-tag { position: absolute; left: 98px; top: 986px; width: 358px; height: 54px; display: flex; align-items: center; justify-content: center; }
  .speaker-band { position: absolute; inset: 0; width: 100%; height: 100%; }
  .speaker-name { position: relative; font-family: "Alfa Slab One", serif; font-size: 25px; line-height: 1; color: var(--ink); white-space: nowrap; }

  .venue { position: absolute; left: 100px; top: 1060px; display: flex; align-items: center; gap: 8px; font-weight: 700; font-size: 13px; color: var(--snow); white-space: nowrap; }

  .register-strip { position: absolute; left: 0; bottom: 0; width: 800px; height: 94px; background: var(--paper); }
  .register-label { position: absolute; left: 100px; top: 1122px; font-weight: 700; font-size: 15px; color: var(--text-dark); letter-spacing: 0.5px; white-space: nowrap; }
  .register-label .leader { letter-spacing: 5px; color: #777; }
  .register-url { position: absolute; left: 100px; top: 1143px; font-weight: 900; font-size: 26px; color: var(--text-dark); white-space: nowrap; }
  .register-url b { color: var(--sky); font-weight: 900; }

  .speaker-photo { position: absolute; left: 470px; top: 800px; width: 330px; height: 400px;
    background: linear-gradient(160deg, #8a7a66 0%, #c9b49a 40%, #d8c3ae 60%, #9aa6b8 100%); }
</style>
</head>
<body>
<main class="poster">
  <div class="sky" role="img" aria-label="Dramatic dusk sky with blue and pink clouds"></div>
  <div class="moon"></div>
  <div class="mountain-forest" role="img" aria-label="Sunlit rocky mountain peaks above a dark pine forest silhouette"></div>
  <div class="crowd-photo" role="img" aria-label="Faded black and white photo of young adults standing together outdoors"></div>

  <div class="brand">PR Brightway</div>
  <div class="presents">······· PRESENTS ·······</div>

  <svg class="title-band" viewBox="0 0 730 275" preserveAspectRatio="none" aria-hidden="true">
    <path d="M60 18 L690 0 L700 40 L680 70 L725 110 L700 180 L720 240 L640 262 L30 275 L0 230 L40 190 L10 130 L45 80 L20 40 Z" fill="#2e3794"/>
  </svg>
  <h1 class="title">
    <span class="title-region">SOUTH DAKOTA</span>
    <span class="title-group">YOUNG ADULT</span>
    <span class="title-main">RETREAT</span>
  </h1>

  <div class="dates">
    <div class="dates-text">
      <div class="dates-days">3-5<sup>TH</sup></div>
      <div class="dates-month">JUNE</div>
    </div>
    <div class="dates-year"><span>2022</span></div>
  </div>

  <div class="speaker-tag">
    <svg class="speaker-band" viewBox="0 0 358 54" preserveAspectRatio="none" aria-hidden="true">
      <path d="M20 4 L358 0 L350 54 L0 52 L14 40 L4 30 L18 18 Z" fill="#2aa9e2"/>
    </svg>
    <span class="speaker-name">MARLA PETTIGREW</span>
  </div>

  <div class="venue">
    <svg width="16" height="18" viewBox="0 0 16 18" aria-hidden="true">
      <path d="M8 1 C4 1 1.5 4 1.5 7.2 C1.5 11.5 8 17 8 17 C8 17 14.5 11.5 14.5 7.2 C14.5 4 12 1 8 1 Z" fill="none" stroke="#2aa9e2" stroke-width="2"/>
      <circle cx="8" cy="7.3" r="2.3" fill="#2aa9e2"/>
    </svg>
    <span>Cedar Ridge Lodge Center, Deadwood, SD</span>
  </div>

  <div class="register-strip"></div>
  <div class="register-label">REGISTER AT <span class="leader">..............</span></div>
  <div class="register-url">www.<b>PRBrightway</b>.com</div>

  <div class="speaker-photo" role="img" aria-label="Photo of speaker Marla Pettigrew seated in a tufted armchair"></div>
</main>
</body>
</html>
```